Marrowind Booking Engine Marketing Site

Hi,
I’m currently in the process of putting together a web application with the intention of providing small resorts/B&Bs/small hotels the ability to allow their customers to book online.
I’m looking to have a design created for a marketing site, to give potential customers additional information about my booking engine, as well as to help drive sign-ups. A lot of the competition out there appears outdated, so I would like something that is more modern and up to date.
I am looking for just the design (i’m a web developer, but I lack the creative skills for a good marketing site)
For some more background, I will be targeting business owners of smaller resorts and Bed & Breakfasts. These are typically family owned small businesses that may only have a 10 room setup. These businesses will also typically have additional amenities that they will have to rent out or sell to their clients ( ex. Spa, fruit basket, water sport rentals). My software will provide them with the ability to sell their amenities as well.
I’m open to different designs, but my main thing is I want it to look modern, and I want it to have several callouts to sign up for my product.
I am looking to have the homepage created, 1 interior page, and a style guide created (to show form fields, H1’s, etc.).
I had a logo created a couple months ago that will be included with this project brief.
If you need any additional information feel free to reach out to me.

Target Market(s)

This site will be targeted small business owners who are running small resorts, Bed and Breakfasts, or any business that provides rooms for their clients.

Industry/Entity Type

Saas

Number of Pages Required

2 page

Font styles to use
Sans Serif

Colors

Designer to choose colors to be used in the design.

Requirements
Must have
• A modern feel, with several CTA's that will drive to the registration page on the homepage. on the internal page, I mostly just need the page layout, I will reuse that page layout. and a style guide if at all possible (include colors, form fields, H1's, etc.)
Nice to have
• maybe a hero image at the top with buttons over the top? again i'm pretty open to most anything.
Should not have
• I like images, but I don't want the page overrun with images. A good balance.

```html
<!DOCTYPE html>
<html lang="en">
<head>
<meta charset="utf-8">
<title>Marrowind Booking Engine</title>
<link href="https://fonts.googleapis.com/css2?family=Roboto:wght@300;400;500;700&family=Open+Sans:wght@400;600;700&display=swap" rel="stylesheet">
<style>
:root{
  --navy:#0d3d73;
  --blue:#1565b8;
  --deep:#0a2f5c;
  --green:#4a9e1f;
  --green-light:#7cc540;
  --teal:#1f8a99;
  --mint:#dfeeee;
  --ink:#222a33;
  --muted:#5d6670;
  --line:#d9dee3;
  --orange:#e8541c;
  --orange-light:#f39a2a;
  --foot:#eef0f2;
  --white:#ffffff;
}
*{box-sizing:border-box;margin:0;padding:0}
html,body{width:1200px;height:4826px;overflow:hidden}
body{font-family:"Open Sans",sans-serif;color:var(--ink);background:var(--white);position:relative}
h1,h2,h3{font-family:"Roboto",sans-serif;font-weight:400}
.abs{position:absolute}
.btn{display:inline-block;border-radius:30px;color:#fff;font:700 15px "Roboto",sans-serif;text-transform:uppercase;text-align:center;letter-spacing:.3px}
.btn-green{background:linear-gradient(#7cc540,#3f8f14);box-shadow:0 3px 6px rgba(0,0,0,.25)}
.lorem{font-size:14px;line-height:24px;color:var(--muted)}
.screen svg{display:block;width:100%;height:100%}

/* header */
.site-header{top:0;left:0;width:1200px;height:71px;background:#fff;border-bottom:1px solid var(--line)}
.brand{left:71px;top:15px;display:flex;align-items:center;gap:10px}
.brand-dot{width:36px;height:36px;border-radius:50%;background:var(--green);flex:none}
.brand-name{font:600 16px/19px "Open Sans",sans-serif;color:var(--blue);white-space:nowrap}
.main-nav{left:312px;top:27px;display:flex;gap:30px;font:500 13px "Roboto",sans-serif;color:var(--ink);text-transform:uppercase}
.nav-btn{top:20px;height:32px;font:700 13px/32px "Roboto",sans-serif;color:#fff;border-radius:3px;text-align:center}
.sign-in{left:890px;width:120px;background:var(--blue)}
.sign-up{left:1025px;width:140px;background:var(--green-light)}

/* hero */
.hero{top:71px;left:0;width:1200px;height:685px;background:linear-gradient(180deg,#0f4f82 0%,#175f8f 45%,#0b3a66 100%)}
.hero h1{top:90px;width:1200px;text-align:center;color:#fff;font-weight:700;font-size:38px}
.hero .sub{top:142px;width:1200px;text-align:center;color:#fff;font:400 30px "Roboto",sans-serif}
.hero .btn{left:478px;top:215px;width:244px;height:46px;line-height:46px}
.device-hero{left:400px;top:330px;width:500px;height:330px;border-radius:14px 14px 0 0;background:linear-gradient(#2b2f36,#14171c);padding:12px 12px 14px}
.laptop-base{left:320px;top:660px;width:660px;height:18px;border-radius:0 0 40px 40px;background:linear-gradient(#e4e7ea,#9fa5ac)}
.callout{left:160px;top:276px;width:280px;height:280px;border-radius:50%;background:#fff;border:10px solid #222;box-shadow:0 6px 20px rgba(0,0,0,.4);padding:70px 0 0 40px;font:400 15px/38px "Roboto",sans-serif;color:var(--blue);z-index:2}
.callout .head{color:var(--ink);font-weight:500;border-bottom:1px solid var(--line);width:190px}

/* features */
.features{top:756px;left:0;width:1200px;height:933px;background:var(--mint)}
.features h2{top:70px;width:1200px;text-align:center;font-size:34px}
.features .lorem{top:112px;left:150px;width:900px;text-align:center}
.device-tablet{left:0;top:418px;width:500px;height:410px;border-radius:0 26px 26px 0;background:linear-gradient(135deg,#3a3f47,#16191e);padding:26px 30px 26px 20px;box-shadow:0 12px 30px rgba(0,0,0,.3)}
.feature{width:160px;text-align:center;font:400 15px/19px "Roboto",sans-serif;color:var(--ink)}
.feature svg{display:block;margin:0 auto 8px}

/* simple */
.simple{top:1689px;left:0;width:1200px;height:585px;background:#fff}
.simple h2{left:71px;top:74px;width:440px;font-size:33px;line-height:42px}
.simple .lorem{left:71px;top:212px;width:440px}
.simple .btn{left:71px;top:474px;width:272px;height:48px;line-height:48px}
.browser{left:563px;top:74px;width:637px;height:376px;border:1px solid var(--line);border-right:0;box-shadow:0 6px 24px rgba(0,0,0,.15);background:#fff}

/* workflow */
.workflow{top:2274px;left:0;width:1200px;height:660px;background:linear-gradient(120deg,#e9eef3,#f6f8fa)}
.workflow .band{left:0;bottom:0;width:1200px;height:87px;background:var(--navy)}
.device-desktop{left:64px;top:123px;width:483px;height:306px;border-radius:12px;background:#1d2026;padding:12px}
.stand{left:256px;top:429px;width:100px;height:86px;background:linear-gradient(#cfd3d8,#a6abb2)}
.workflow h2{left:611px;top:84px;font-size:34px}
.ticks{left:611px;top:136px;list-style:none;font-size:15px;color:var(--ink)}
.ticks li{height:39px;display:flex;align-items:center;gap:12px}
.workflow .btn{left:611px;top:490px;width:268px;height:48px;line-height:48px}

/* testimonials */
.testimonials{top:2934px;left:0;width:1200px;height:679px;background:#fff}
.testimonials h2{top:70px;width:1200px;text-align:center;font-size:34px;line-height:44px}
.quote-card{top:200px;width:330px;text-align:center}
.quote-card .qi{width:42px;height:42px;margin:0 auto 16px;border-radius:50%;background:var(--blue);color:#fff;font:700 26px/50px Georgia,serif}
.quote-card p{font-size:14px;line-height:22px;color:var(--muted)}
.quote-card .avatar{width:52px;height:52px;border-radius:50%;background:linear-gradient(#c9d3dd,#9aa7b4);margin:26px auto 10px}
.quote-card .name{font:500 19px "Roboto",sans-serif;color:var(--blue)}
.quote-card .role{font-size:13px;color:var(--muted)}
.divider{top:200px;width:1px;height:360px;background:var(--line)}
.dots{top:590px;left:548px;display:flex;gap:8px}
.dots span{width:14px;height:14px;border-radius:50%;border:1px solid #9aa7b4}
.dots span.on{background:var(--blue);border-color:var(--blue)}

/* success */
.success{top:3613px;left:0;width:1200px;height:627px;background:linear-gradient(90deg,#176f7d 0%,#1f8a99 55%,#2b9aa5 100%)}
.success h2{top:78px;width:1200px;text-align:center;color:#fff;font-size:34px}
.success .intro{top:128px;left:310px;width:580px;text-align:center;color:#fff;font-size:15px;line-height:24px}
.success .cap{left:0;width:1200px;text-align:center;color:#fff;font:700 15px/24px "Open Sans",sans-serif}

/* cta */
.cta{top:4240px;left:0;width:1200px;height:161px;background:linear-gradient(90deg,var(--orange),var(--orange-light))}
.cta h2{left:71px;top:40px;color:#fff;font-weight:700;font-size:32px}
.cta p{left:71px;top:88px;color:#fff;font-size:19px}
.cta .btn{left:830px;top:48px;width:296px;height:64px;line-height:64px;font-size:18px}

/* footer */
.site-footer{top:4401px;left:0;width:1200px;height:425px;background:var(--foot)}
.col h4{font:700 15px "Roboto",sans-serif;margin-bottom:12px}
.col p,.col li{font-size:13px;line-height:22px;color:var(--muted);list-style:none}
.phone-label{font-size:14px;color:var(--muted)}
.phone{font:400 30px "Roboto",sans-serif;color:var(--ink);margin-bottom:8px}
.socials{display:flex;gap:10px;margin-bottom:16px}
.socials span{width:38px;height:38px;border-radius:50%;border:2px solid #444}
.copyright{left:71px;top:372px;font-size:13px;color:var(--muted)}
.site-footer .btn{left:885px;top:358px;width:240px;height:46px;line-height:46px}
</style>
</head>
<body>

<svg width="0" height="0" style="position:absolute" aria-hidden="true">
  <defs>
    <symbol id="calendar-ui" viewBox="0 0 480 300" preserveAspectRatio="none">
      <rect width="480" height="300" fill="#fff"/>
      <rect width="480" height="16" fill="#eef1f4"/>
      <rect x="8" y="5" width="40" height="6" rx="2" fill="#1565b8"/>
      <rect x="400" y="4" width="34" height="8" rx="2" fill="#1565b8"/>
      <rect x="440" y="4" width="32" height="8" rx="2" fill="#7cc540"/>
      <rect x="0" y="16" width="66" height="284" fill="#f6f8fa"/>
      <g fill="#c9d0d7"><rect x="8" y="28" width="44" height="4"/><rect x="8" y="40" width="38" height="4"/><rect x="8" y="52" width="46" height="4"/><rect x="8" y="64" width="36" height="4"/><rect x="8" y="76" width="42" height="4"/></g>
      <rect x="76" y="26" width="90" height="12" fill="none" stroke="#c9d0d7"/>
      <rect x="176" y="26" width="70" height="12" fill="none" stroke="#c9d0d7"/>
      <rect x="420" y="26" width="50" height="12" rx="2" fill="#1565b8"/>
      <rect x="76" y="48" width="394" height="14" fill="#e9eef3"/>
      <g stroke="#e3e7eb">
        <path d="M76 76h394M76 90h394M76 104h394M76 118h394M76 132h394M76 146h394M76 160h394M76 174h394M76 188h394M76 202h394M76 216h394"/>
        <path d="M136 48v168M176 48v168M216 48v168M256 48v168M296 48v168M336 48v168M376 48v168M416 48v168"/>
      </g>
      <g fill="#b5bdc5"><rect x="80" y="67" width="40" height="4"/><rect x="80" y="81" width="34" height="4"/><rect x="80" y="95" width="44" height="4"/><rect x="80" y="109" width="36" height="4"/><rect x="80" y="123" width="42" height="4"/><rect x="80" y="137" width="38" height="4"/><rect x="80" y="151" width="44" height="4"/><rect x="80" y="165" width="34" height="4"/></g>
      <rect x="176" y="64" width="120" height="10" fill="#f0c419"/>
      <rect x="216" y="78" width="80" height="10" fill="#7cc540"/>
      <rect x="296" y="78" width="80" height="10" fill="#e84c4c"/>
      <rect x="136" y="92" width="120" height="10" fill="#7cc540"/>
      <rect x="256" y="106" width="120" height="10" fill="#4aa3df"/>
      <rect x="176" y="120" width="80" height="10" fill="#9b59b6"/>
      <rect x="296" y="134" width="120" height="10" fill="#7cc540"/>
      <rect x="216" y="148" width="80" height="10" fill="#e84c4c"/>
      <rect x="336" y="162" width="80" height="10" fill="#4aa3df"/>
      <rect x="136" y="176" width="120" height="10" fill="#f0c419"/>
      <g><rect x="76" y="240" width="30" height="8" fill="#7cc540"/><rect x="114" y="240" width="30" height="8" fill="#e84c4c"/><rect x="152" y="240" width="30" height="8" fill="#4aa3df"/><rect x="190" y="240" width="30" height="8" fill="#9b59b6"/><rect x="228" y="240" width="30" height="8" fill="#f0c419"/></g>
    </symbol>
  </defs>
</svg>

<header class="site-header abs">
  <div class="brand abs"><span class="brand-dot"></span><span class="brand-name">Marrowind<br>Booking Engine</span></div>
  <nav class="main-nav abs"><span>Home</span><span>Features</span><span>About Us</span><span>Support</span><span>Testimonials</span><span>Contact Us</span></nav>
  <div class="nav-btn sign-in abs">SIGN IN</div>
  <div class="nav-btn sign-up abs">FREE SIGN UP</div>
</header>

<section class="hero abs" role="img" aria-label="Photo of a lakeside resort at dusk">
  <h1 class="abs">We Providing Small Resorts/B&amp;Bs/Small Hotels</h1>
  <div class="sub abs">The Ability to Allow Their Customers to Book Online.</div>
  <a class="btn btn-green abs">Start your free trial</a>
  <div class="device-hero screen abs"><svg><use href="#calendar-ui"/></svg></div>
  <div class="laptop-base abs"></div>
  <div class="callout abs">
    <div class="head">Reservations</div>
    <div>Booking Calendar</div>
    <div>Reservations</div>
    <div>Customers</div>
  </div>
</section>

<section class="features abs">
  <h2 class="abs">A Powerful And Innovative Features Set</h2>
  <p class="lorem abs">Lorem ipsum dolor sit amet, consectetur adipiscing elit, sed do eiusmod tempor incididunt ut labore et dolore magna aliqua. Ut enim ad minim veniam, quis nostrud exercitation ullamco laboris nisi ut aliquip ex ea commodo consequat.</p>
  <div class="device-tablet screen abs">
    <svg viewBox="0 0 450 360" preserveAspectRatio="none">
      <rect width="450" height="360" fill="#fff"/>
      <rect width="450" height="20" fill="#eef1f4"/>
      <rect x="10" y="7" width="50" height="6" rx="2" fill="#1565b8"/>
      <rect x="0" y="20" width="70" height="340" fill="#f6f8fa"/>
      <g fill="#c9d0d7"><rect x="10" y="34" width="46" height="5"/><rect x="10" y="48" width="40" height="5"/><rect x="10" y="62" width="48" height="5"/><rect x="10" y="76" width="36" height="5"/></g>
      <rect x="84" y="32" width="120" height="8" fill="#b5bdc5"/>
      <rect x="380" y="30" width="56" height="14" rx="2" fill="#1565b8"/>
      <rect x="84" y="60" width="352" height="130" fill="none" stroke="#e3e7eb"/>
      <rect x="94" y="70" width="130" height="110" fill="#8a5a3c" role="img" aria-label="Hotel room photo"/>
      <rect x="236" y="76" width="120" height="7" fill="#1565b8"/>
      <g fill="#c9d0d7"><rect x="236" y="92" width="180" height="4"/><rect x="236" y="102" width="160" height="4"/><rect x="236" y="112" width="170" height="4"/></g>
      <rect x="236" y="150" width="60" height="16" rx="2" fill="#7cc540"/>
      <rect x="84" y="204" width="352" height="130" fill="none" stroke="#e3e7eb"/>
      <rect x="94" y="214" width="130" height="110" fill="#a0694a" role="img" aria-label="Hotel room photo"/>
      <rect x="236" y="220" width="120" height="7" fill="#1565b8"/>
      <g fill="#c9d0d7"><rect x="236" y="236" width="180" height="4"/><rect x="236" y="246" width="160" height="4"/><rect x="236" y="256" width="170" height="4"/></g>
      <rect x="236" y="294" width="60" height="16" rx="2" fill="#7cc540"/>
    </svg>
  </div>

  <div class="feature abs" style="left:500px;top:300px"><svg width="92" height="92"><circle cx="46" cy="46" r="44" fill="#0d3d73"/><rect x="30" y="32" width="32" height="28" rx="3" fill="none" stroke="#fff" stroke-width="3"/><line x1="30" y1="41" x2="62" y2="41" stroke="#fff" stroke-width="3"/></svg>Booking<br>Management</div>
  <div class="feature abs" style="left:660px;top:300px"><svg width="92" height="92"><circle cx="46" cy="46" r="44" fill="#0d3d73"/><path d="M28 56h36M32 56c0-10 6-16 14-16s14 6 14 16" fill="none" stroke="#fff" stroke-width="3"/></svg>Amenity<br>Management</div>
  <div class="feature abs" style="left:820px;top:300px"><svg width="92" height="92"><circle cx="46" cy="46" r="44" fill="#0d3d73"/><rect x="32" y="28" width="28" height="36" fill="none" stroke="#fff" stroke-width="3"/><path d="M38 36h4M50 36h4M38 44h4M50 44h4M38 52h4M50 52h4" stroke="#fff" stroke-width="3"/></svg>Property<br>Management</div>
  <div class="feature abs" style="left:966px;top:300px"><svg width="92" height="92"><circle cx="46" cy="46" r="44" fill="#0d3d73"/><circle cx="46" cy="36" r="8" fill="none" stroke="#fff" stroke-width="3"/><path d="M32 62c0-10 6-14 14-14s14 4 14 14" fill="none" stroke="#fff" stroke-width="3"/></svg>Online<br>Booking</div>

  <div class="feature abs" style="left:500px;top:490px"><svg width="92" height="92"><circle cx="46" cy="46" r="44" fill="#0d3d73"/><rect x="34" y="28" width="24" height="36" fill="none" stroke="#fff" stroke-width="3"/><path d="M39 38h14M39 46h14M39 54h8" stroke="#fff" stroke-width="3"/></svg>Invoicing</div>
  <div class="feature abs" style="left:660px;top:490px"><svg width="92" height="92"><circle cx="46" cy="46" r="44" fill="#0d3d73"/><circle cx="46" cy="46" r="14" fill="none" stroke="#fff" stroke-width="3"/><circle cx="46" cy="28" r="4" fill="#fff"/><circle cx="46" cy="64" r="4" fill="#fff"/><circle cx="28" cy="46" r="4" fill="#fff"/><circle cx="64" cy="46" r="4" fill="#fff"/></svg>Multi-User<br>Capabilities</div>
  <div class="feature abs" style="left:820px;top:490px"><svg width="92" height="92"><circle cx="46" cy="46" r="44" fill="#0d3d73"/><rect x="28" y="38" width="14" height="26" fill="none" stroke="#fff" stroke-width="3"/><rect x="46" y="28" width="18" height="36" fill="none" stroke="#fff" stroke-width="3"/></svg>Multi-Property<br>Capabilities</div>
  <div class="feature abs" style="left:966px;top:490px"><svg width="92" height="92"><circle cx="46" cy="46" r="44" fill="#0d3d73"/><path d="M30 60V44l16-12 16 12v16z" fill="none" stroke="#fff" stroke-width="3"/><path d="M46 44v12M40 50h12" stroke="#fff" stroke-width="3"/></svg>Ability to<br>Add/Manage<br>Rooms/Units</div>

  <div class="feature abs" style="left:500px;top:683px"><svg width="92" height="92"><circle cx="46" cy="46" r="44" fill="#0d3d73"/><path d="M30 58l32-24M34 36l4 4M54 54l4 4" stroke="#fff" stroke-width="3"/></svg>Rates<br>Management</div>
  <div class="feature abs" style="left:660px;top:683px"><svg width="92" height="92"><circle cx="46" cy="46" r="44" fill="#0d3d73"/><path d="M28 62h36M30 56l10-12 8 6 14-16" fill="none" stroke="#fff" stroke-width="3"/></svg>Integrated<br>Analytics<br>Tracking</div>
  <div class="feature abs" style="left:820px;top:683px"><svg width="92" height="92"><circle cx="46" cy="46" r="44" fill="#0d3d73"/><rect x="32" y="28" width="28" height="36" rx="2" fill="none" stroke="#fff" stroke-width="3"/><path d="M38 54V48M46 54V40M54 54V44" stroke="#fff" stroke-width="3"/></svg>Reporting</div>
  <div class="feature abs" style="left:966px;top:683px"><svg width="92" height="92"><circle cx="46" cy="46" r="44" fill="#0d3d73"/><path d="M30 60l32-28M32 40l6-6M54 58l6-6" stroke="#fff" stroke-width="3"/><circle cx="36" cy="36" r="5" fill="none" stroke="#fff" stroke-width="3"/><circle cx="56" cy="56" r="5" fill="none" stroke="#fff" stroke-width="3"/></svg>Promotions<br>Capabilities</div>
</section>

<section class="simple abs">
  <h2 class="abs">Simple, Powerful, Reliable Marrowind Booking Engine system</h2>
  <p class="lorem abs">Lorem ipsum dolor sit amet, consectetur adipiscing elit, sed do eiusmod tempor incididunt ut labore et dolore magna aliqua. Ut enim ad minim veniam, quis nostrud exercitation ullamco laboris nisi ut aliquip ex ea commodo consequat. Duis aute irure dolor in reprehenderit in voluptate velit esse cillum dolore eu fugiat nulla pariatur. Excepteur sint occaecat cupidatat non proident, sunt in culpa qui officia deserunt mollit anim id est laborum.</p>
  <a class="btn btn-green abs">Start your free trial</a>
  <div class="browser screen abs">
    <svg viewBox="0 0 636 374" preserveAspectRatio="none">
      <rect width="636" height="374" fill="#fff"/>
      <rect width="636" height="30" fill="#eceff2"/>
      <circle cx="14" cy="15" r="5" fill="#e84c4c"/><circle cx="30" cy="15" r="5" fill="#f0c419"/><circle cx="46" cy="15" r="5" fill="#7cc540"/>
      <rect x="70" y="8" width="24" height="14" rx="3" fill="#fff" stroke="#cfd5db"/>
      <rect x="100" y="8" width="24" height="14" rx="3" fill="#fff" stroke="#cfd5db"/>
      <rect x="200" y="8" width="240" height="14" rx="3" fill="#fff" stroke="#cfd5db"/>
      <rect x="290" y="13" width="60" height="4" fill="#b5bdc5"/>
      <rect x="0" y="30" width="636" height="14" fill="#f6f8fa"/>
      <rect x="8" y="34" width="46" height="6" rx="2" fill="#1565b8"/>
      <rect x="0" y="44" width="90" height="330" fill="#fafbfc"/>
      <rect x="90" y="44" width="1" height="330" fill="#e3e7eb"/>
      <g fill="#c9d0d7"><rect x="10" y="56" width="60" height="4"/><rect x="10" y="68" width="50" height="4"/><rect x="10" y="80" width="56" height="4"/><rect x="10" y="92" width="44" height="4"/></g>
      <rect x="104" y="56" width="70" height="6" fill="#8c959e"/>
      <rect x="560" y="54" width="64" height="12" rx="2" fill="#1565b8"/>
      <rect x="104" y="76" width="90" height="5" fill="#b5bdc5"/>
      <rect x="104" y="88" width="100" height="10" fill="none" stroke="#cfd5db"/>
      <rect x="104" y="112" width="520" height="14" fill="#e9eef3"/>
      <g stroke="#e3e7eb"><path d="M104 140h520M104 154h520M104 168h520"/></g>
      <g fill="#b5bdc5"><rect x="110" y="131" width="40" height="4"/><rect x="200" y="131" width="60" height="4"/><rect x="320" y="131" width="50" height="4"/><rect x="430" y="131" width="40" height="4"/><rect x="110" y="145" width="36" height="4"/><rect x="200" y="145" width="54" height="4"/><rect x="320" y="145" width="46" height="4"/><rect x="430" y="145" width="44" height="4"/></g>
      <rect x="598" y="128" width="22" height="10" rx="2" fill="#1565b8"/>
      <rect x="598" y="142" width="22" height="10" rx="2" fill="#1565b8"/>
      <rect x="300" y="190" width="140" height="4" fill="#c9d0d7"/>
    </svg>
  </div>
</section>

<section class="workflow abs">
  <div class="stand abs"></div>
  <div class="device-desktop screen abs"><svg><use href="#calendar-ui"/></svg></div>
  <h2 class="abs">Smart And Efficient Workfliw:</h2>
  <ul class="ticks abs">
    <li><svg width="18" height="18"><circle cx="9" cy="9" r="9" fill="#4a9e1f"/><path d="M5 9l3 3 5-6" fill="none" stroke="#fff" stroke-width="2"/></svg>Lorem ipsum dolor sit amet, consectetur adipiscing elit.</li>
    <li><svg width="18" height="18"><circle cx="9" cy="9" r="9" fill="#4a9e1f"/><path d="M5 9l3 3 5-6" fill="none" stroke="#fff" stroke-width="2"/></svg>Sed aliquet dolor in ullamcorper egestas.</li>
    <li><svg width="18" height="18"><circle cx="9" cy="9" r="9" fill="#4a9e1f"/><path d="M5 9l3 3 5-6" fill="none" stroke="#fff" stroke-width="2"/></svg>In consequat fermentum, consequat lacus lobortis, vehicula ante.</li>
    <li><svg width="18" height="18"><circle cx="9" cy="9" r="9" fill="#4a9e1f"/><path d="M5 9l3 3 5-6" fill="none" stroke="#fff" stroke-width="2"/></svg>Fusce a nibh in orci scelerisque imperdiet auctor ut eros.</li>
    <li><svg width="18" height="18"><circle cx="9" cy="9" r="9" fill="#4a9e1f"/><path d="M5 9l3 3 5-6" fill="none" stroke="#fff" stroke-width="2"/></svg>Fusce lacinia massa eget dolor ullamcorper, vitae faucibus.</li>
    <li><svg width="18" height="18"><circle cx="9" cy="9" r="9" fill="#4a9e1f"/><path d="M5 9l3 3 5-6" fill="none" stroke="#fff" stroke-width="2"/></svg>Etiam sollicitudin nisl eu interdum fermentum.</li>
    <li><svg width="18" height="18"><circle cx="9" cy="9" r="9" fill="#4a9e1f"/><path d="M5 9l3 3 5-6" fill="none" stroke="#fff" stroke-width="2"/></svg>Sed a orci mattis, egestas augue ut, sodales sapien.</li>
    <li><svg width="18" height="18"><circle cx="9" cy="9" r="9" fill="#4a9e1f"/><path d="M5 9l3 3 5-6" fill="none" stroke="#fff" stroke-width="2"/></svg>Etiam sollicitudin nisl eu interdum fermentum.</li>
  </ul>
  <a class="btn btn-green abs">Start your free trial</a>
  <div class="band abs"></div>
</section>

<section class="testimonials abs">
  <h2 class="abs">Customer Say Something<br>- Testimonials</h2>
  <div class="quote-card abs" style="left:67px"><div class="qi">“</div><p>" Class aptent taciti sociosqu ad litora torquent per conubia nostra, per inceptos himenaeos. Mauris in erat justo. Nullam ac fermentum nunc. Etiam pharetra, erat sed fermentum feugiat, velit mauris egestas quam, ut aliquam massa nisl quis neque."</p><div class="avatar" role="img" aria-label="Customer portrait"></div><div class="name">Nolan Prescott</div><div class="role">Lorem ipsum dolor sit</div></div>
  <div class="divider abs" style="left:416px"></div>
  <div class="quote-card abs" style="left:434px"><div class="qi">“</div><p>" Class aptent taciti sociosqu ad litora torquent per conubia nostra, per inceptos himenaeos. Mauris in erat justo. Nullam ac fermentum nunc. Etiam pharetra, erat sed fermentum feugiat, velit mauris egestas quam, ut aliquam massa nisl quis neque."</p><div class="avatar" role="img" aria-label="Customer portrait"></div><div class="name">Nolan Prescott</div><div class="role">Lorem ipsum dolor sit</div></div>
  <div class="divider abs" style="left:783px"></div>
  <div class="quote-card abs" style="left:800px"><div class="qi">“</div><p>" Class aptent taciti sociosqu ad litora torquent per conubia nostra, per inceptos himenaeos. Mauris in erat justo. Nullam ac fermentum nunc. Etiam pharetra, erat sed fermentum feugiat, velit mauris egestas quam, ut aliquam massa nisl quis neque."</p><div class="avatar" role="img" aria-label="Customer portrait"></div><div class="name">Nolan Prescott</div><div class="role">Lorem ipsum dolor sit</div></div>
  <div class="dots abs"><span class="on"></span><span></span><span></span><span></span><span></span></div>
</section>

<section class="success abs" role="img" aria-label="Photo of a support agent with a headset giving a thumbs up">
  <h2 class="abs">Customer Success Team</h2>
  <p class="intro abs">Lorem ipsum dolor sit amet, consectetur adipiscing elit, sed do eiusmod tempor incididunt ut labore et dolore magna aliqua.</p>
  <svg class="abs" style="left:560px;top:200px" width="80" height="80"><rect x="14" y="16" width="52" height="36" rx="3" fill="none" stroke="#fff" stroke-width="3"/><path d="M6 60h68" stroke="#fff" stroke-width="3"/><circle cx="40" cy="32" r="7" fill="none" stroke="#fff" stroke-width="3"/></svg>
  <div class="cap abs" style="top:320px">7 days a week support.</div>
  <svg class="abs" style="left:560px;top:390px" width="80" height="80"><rect x="30" y="10" width="44" height="30" fill="none" stroke="#fff" stroke-width="3"/><circle cx="20" cy="30" r="8" fill="none" stroke="#fff" stroke-width="3"/><path d="M6 70V52c0-8 6-12 14-12s14 4 14 12v18" fill="none" stroke="#fff" stroke-width="3"/></svg>
  <div class="cap abs" style="top:500px">Train your team and works with them for as long as needed for them to<br>make the best use of Marrowind Booking Engine.</div>
</section>

<section class="cta abs">
  <h2 class="abs">Ready to get started?</h2>
  <p class="abs">Schedule a demo, and try Marrowind Booking Engine for free</p>
  <a class="btn btn-green abs">Contact us</a>
</section>

<footer class="site-footer abs">
  <div class="col abs" style="left:71px;top:36px;width:270px">
    <div style="display:flex;align-items:center;gap:10px;margin-bottom:30px"><span class="brand-dot"></span><span class="brand-name">Marrowind<br>Booking Engine</span></div>
    <h4>About Us</h4>
    <p>Lorem ipsum dolor sit amet, consectetur adipiscing elit, sed do eiusmod tempor incididunt ut labore et dolore magna aliqua. Ut enim ad minim veniam, quis nostrud exercitation ullamco laboris nisi ut aliquip ex ea commodo consequat. Duis aute irure.</p>
  </div>
  <div class="col abs" style="left:392px;top:36px;width:200px">
    <h4>Contact Us</h4>
    <p><b>Marrowind Booking Engine</b><br>226, lorem ipsum dolor sit,<br>duis amet - 94816</p>
    <p style="margin-top:12px">E : info@marrowind.com</p>
  </div>
  <div class="col abs" style="left:618px;top:36px">
    <h4>Quick Links</h4>
    <ul><li>Home</li><li>Features</li><li>About Us</li><li>Support</li><li>Testimonials</li><li>Contact Us</li></ul>
  </div>
  <div class="col abs" style="left:746px;top:36px">
    <h4>Info Links</h4>
    <ul><li>Terms of Use</li><li>Privacy Policy</li><li>Sitemap</li><li>Help!</li></ul>
  </div>
  <div class="col abs" style="left:885px;top:36px">
    <h4>Get connected with us</h4>
    <div class="socials"><span></span><span></span><span></span><span></span></div>
    <div class="phone-label">Tech Support:</div>
    <div class="phone">(800) 555-0142</div>
    <div class="phone-label">General Support</div>
    <div class="phone">(800) 555-0187</div>
  </div>
  <div class="copyright abs">Copyright © 2018 Marrowind Booking Engine. All Rights Reserved.</div>
  <a class="btn btn-green abs">Start your free trial</a>
</footer>

</body>
</html>
```